ad for food show brochure

Need to clean up this concept sketch. We are selling food at a festival but the concept isn't quite named. We're looking to create a buzz and have people sign up to be kept apprised of the progress of the chain ... or the first store. The website at the bottom is just for filler, we can add that before ad goes to print. We're not married to this text so if you come up with something better, great. also may want to have a blank @ line for twitter feed and another line for FB page.
The concept is for a Vegan Fast Food place but I need to focus more on the middle of the road diners, we'll get the vegans to come and staunch carnivores won't ever come so it's the middle of the road folks we're after. The slant and speed lines were my attempt to show speed.
Thanks.
This ad is a 5/5 x 2.125 space in the festival brochure. Need this asap.
I also think this needs to be b&w so lets go with that. Just found out COLOR is ok.
That last word in the sketch is not whose but WHERE?
The last word is WHERE not whose. Thanks
We either need to add the word Vegan in the top of the ad or add it in the sentence about all that is vegan and good in the worl.
The ad can be in color. Just to clarify, the word Vegan should be o e of the questions on top. Eithe as part of another question ... 'Vegan fast food?' Or as its own line or bubble.
- pdf file so I can change the website address.

```html
<!DOCTYPE html>
<html lang="en">
<head>
<meta charset="utf-8">
<title>Vegan Fast Food – Coming Soon</title>
<link rel="stylesheet" href="https://fonts.googleapis.com/css2?family=Archivo+Black&family=Oswald:wght@500&family=PT+Sans&family=PT+Serif:wght@700&display=swap">
<style>
  :root {
    --backdrop: #d9d4cc;
    --paper: #ffffff;
    --ink: #111111;
    --ink-soft: #222222;
    --silhouette: #e0e0e0;
    --silhouette-fade: #ebebeb;
  }
  html, body {
    margin: 0;
    width: 1200px;
    height: 2708px;
    overflow: hidden;
    background: var(--backdrop);
  }
  .ad {
    position: absolute;
    left: 108px;
    top: 55px;
    width: 985px;
    height: 2597px;
    background: var(--paper);
    overflow: hidden;
    color: var(--ink);
    font-family: "PT Sans", Arial, sans-serif;
  }
  .ad > * { position: absolute; margin: 0; white-space: nowrap; }

  .landmark-silhouette {
    left: 200px;
    top: 40px;
    width: 540px;
    height: 2480px;
    border-radius: 120px 160px 40px 40px;
    background: linear-gradient(180deg, var(--silhouette-fade) 0%, var(--silhouette) 30%, var(--silhouette) 100%);
  }

  .headline {
    left: 60px;
    top: 60px;
    transform: rotate(13deg);
    transform-origin: left top;
    font-family: "Archivo Black", "Arial Black", sans-serif;
    font-style: italic;
    font-weight: 400;
    line-height: 0.95;
    text-transform: uppercase;
  }
  .headline span {
    display: block;
    transform: skewX(-14deg);
    background: repeating-linear-gradient(180deg, var(--ink) 0 9px, var(--paper) 9px 13px);
    -webkit-background-clip: text;
    background-clip: text;
    color: transparent;
  }
  .headline .word-vegan { font-size: 132px; letter-spacing: 3px; }
  .headline .word-fast { font-size: 140px; margin-left: 40px; letter-spacing: 14px; }
  .headline .word-food { font-size: 140px; margin-left: 70px; letter-spacing: 10px; }

  .reply {
    font-size: 58px;
    line-height: 1;
    color: var(--ink-soft);
    transform: rotate(-10deg);
  }
  .reply-yep { left: 700px; top: 500px; }
  .reply-yop-1 { left: 640px; top: 705px; }
  .reply-yop-2 { left: 660px; top: 1050px; }

  .question-soon {
    left: 170px;
    top: 840px;
    font-size: 90px;
    line-height: 1;
    transform: rotate(-27deg);
    transform-origin: left bottom;
    color: var(--ink-soft);
  }
  .question-city {
    left: 120px;
    top: 1016px;
    font-family: "Oswald", "Arial Narrow", sans-serif;
    font-weight: 500;
    font-size: 190px;
    line-height: 1;
    transform: rotate(-20deg);
    transform-origin: left bottom;
  }
  .plea {
    left: 140px;
    top: 1390px;
    font-size: 68px;
    line-height: 95px;
    transform: rotate(-22deg);
    transform-origin: left top;
    color: var(--ink-soft);
  }
  .plea strong {
    font-family: "PT Serif", Georgia, serif;
    font-weight: 700;
    font-size: 90px;
    line-height: 0;
  }
  .question-where {
    left: 431px;
    top: 1718px;
    font-size: 110px;
    line-height: 1;
    transform: rotate(-18deg);
    transform-origin: left bottom;
    color: var(--ink-soft);
  }

  .social {
    left: 0;
    top: 2052px;
    width: 100%;
    display: flex;
    justify-content: center;
    gap: 60px;
    font-size: 36px;
  }
  .social span { display: inline-flex; align-items: center; gap: 12px; }
  .social i {
    display: inline-block;
    width: 30px;
    height: 30px;
    background: var(--ink);
  }
  .website {
    left: 0;
    top: 2115px;
    width: 100%;
    text-align: center;
    font-size: 50px;
  }
  .until {
    left: 108px;
    top: 2200px;
    font-size: 75px;
    line-height: 1.1;
  }
  .drumstix {
    left: 431px;
    top: 2305px;
    font-size: 50px;
    line-height: 1.1;
  }
  .today {
    left: 0;
    top: 2370px;
    width: 100%;
    text-align: center;
    font-size: 140px;
    line-height: 1.1;
  }
</style>
</head>
<body>
  <main class="ad">
    <div class="landmark-silhouette" role="img" aria-label="Faint grey silhouette of the Statue of Liberty behind the text"></div>

    <h1 class="headline">
      <span class="word-vegan">Vegan</span>
      <span class="word-fast">Fast</span>
      <span class="word-food">Food ?</span>
    </h1>

    <p class="reply reply-yep">Yep</p>
    <p class="question-soon">Coming Soon ?</p>
    <p class="reply reply-yop-1">Yop</p>
    <p class="question-city">IN NYC ?</p>
    <p class="reply reply-yop-2">Yop</p>

    <p class="plea">In the name of all that<br>is <strong>Vegan</strong> and good<br>in the world .........</p>
    <p class="question-where">Where ??</p>

    <p class="social">
      <span><i></i>/ plantlane-eats</span>
      <span><i></i>@plantlane-eats</span>
    </p>
    <p class="website">www.plantlane-eats.com</p>
    <p class="until">Until then ........</p>
    <p class="drumstix">enjoy our drumstix</p>
    <p class="today">Today</p>
  </main>
</body>
</html>
```